Website for Larkwood Fresh Foods

Slogan to be used is Fresh is Best !
I would like the website to be like my other business @ www.tuberhaven.com.au. It is the same business

Industry/Entity Type

Vegetable Processing

Coding

Coded - Design and coding required

Number of Pages Required

1 page

```html
<!DOCTYPE html>
<html lang="en">
<head>
<meta charset="utf-8">
<title>Crispfield – Fresh is Best !</title>
<link href="https://fonts.googleapis.com/css2?family=Lato:wght@400;700&family=Playfair+Display:ital,wght@0,700;0,900;1,700&display=swap" rel="stylesheet">
<style>
  :root {
    --green: #6fa31c;
    --green-dark: #5d9215;
    --green-band: #5f8a45;
    --leaf: #7db227;
    --ink: #1d1d1d;
    --paper: #f3f3f1;
    --white: #ffffff;
  }
  * { box-sizing: border-box; margin: 0; padding: 0; }
  html, body { width: 1200px; height: 1054px; overflow: hidden; }
  body {
    position: relative;
    background: var(--paper);
    font-family: "Lato", sans-serif;
    color: var(--ink);
  }
  .produce-top, .produce-bottom { position: absolute; left: 0; width: 1200px; }
  .produce-top {
    top: 0; height: 120px;
    background: linear-gradient(90deg, #e9c548 0%, #c9a07a 20%, #d8473a 40%, #f0c23a 60%, #b98a6a 80%, #8a3d55 100%);
    opacity: .55;
  }
  .produce-bottom {
    top: 805px; height: 249px;
    background: linear-gradient(90deg, #d9453a 0%, #5e8c34 18%, #f1a23a 35%, #f3cb3a 48%, #7c3550 58%, #8ab954 70%, #d23a30 82%, #f1a23a 100%);
    opacity: .6;
  }
  .site {
    position: absolute; left: 162px; top: 71px; width: 876px; height: 629px;
    border-radius: 26px; overflow: hidden;
    background: var(--white);
    box-shadow: 0 6px 20px rgba(0,0,0,.18);
  }
  .promo-bar {
    height: 38px; background: var(--green);
    display: flex; align-items: center; justify-content: center;
    font-family: "Playfair Display", serif; font-style: italic; font-weight: 700;
    font-size: 13.5px; color: var(--white);
  }
  .header {
    height: 55px; display: flex; align-items: center;
    padding: 0 34px; background: #fafaf8;
  }
  .brand {
    font-family: "Lato", sans-serif; font-weight: 700; font-size: 30px;
    color: var(--green); width: 250px;
  }
  .main-nav { display: flex; gap: 21px; font-size: 10px; font-weight: 700; }
  .main-nav a { color: var(--ink); text-decoration: none; }
  .main-nav a.active { color: var(--green); }
  .call { margin-left: auto; display: flex; align-items: center; gap: 8px; }
  .call-icon {
    width: 33px; height: 33px; border-radius: 50%; background: var(--green);
    display: flex; align-items: center; justify-content: center;
  }
  .call-label { font-size: 11.5px; line-height: 1; }
  .call-number {
    font-family: "Playfair Display", serif; font-weight: 700;
    font-size: 19px; color: var(--green); line-height: 1.1;
  }
  .body { display: flex; height: 477px; }
  .categories { width: 176px; background: var(--leaf); color: var(--white); }
  .categories h2 {
    height: 41px; background: var(--green-dark);
    font-family: "Playfair Display", serif; font-weight: 900; font-size: 15px;
    padding: 10px 0 0 28px;
  }
  .categories ul { list-style: none; padding: 19px 0 0 28px; }
  .categories li { font-size: 12px; font-weight: 700; height: 31.25px; }
  .hero {
    flex: 1; position: relative;
    background: linear-gradient(180deg, #a9cf48 0%, #7f9a3a 30%, #b2643a 55%, #8a5a34 75%, #6b4326 100%);
  }
  .hero-title {
    position: absolute; left: 60px; top: 276px;
    font-family: "Playfair Display", serif; font-weight: 900; font-size: 84px;
    color: var(--white); line-height: 1; white-space: nowrap;
  }
  .why {
    height: 59px; background: var(--green-band); color: var(--white);
    display: flex; align-items: center; padding-left: 25px;
  }
  .why h2 {
    font-family: "Playfair Display", serif; font-weight: 900; font-size: 19px;
    width: 178px;
  }
  .reason {
    display: flex; align-items: center; gap: 8px; height: 40px;
    font-family: "Playfair Display", serif; font-weight: 700; font-size: 12.5px; line-height: 1.3;
  }
  .reason.one { width: 207px; }
  .reason.two { width: 223px; padding-left: 42px; border-left: 1px solid rgba(255,255,255,.8); }
  .reason.three { padding-left: 35px; border-left: 1px solid rgba(255,255,255,.8); }
  .footer { position: absolute; left: 0; width: 1200px; top: 733px; text-align: center; }
  .footer-cats {
    display: flex; justify-content: center;
    font-family: "Playfair Display", serif; font-weight: 700; font-size: 10.5px;
  }
  .footer-cats span + span::before { content: "|"; margin: 0 10px; font-family: "Lato", sans-serif; font-weight: 400; color: #666; }
  .footer-nav { margin-top: 14px; font-size: 10px; font-weight: 700; display: flex; justify-content: center; gap: 21px; }
  .copyright { margin-top: 14px; font-size: 10px; }
  .copyright .name { color: var(--green); }
</style>
</head>
<body>
  <div class="produce-top" role="img" aria-label="Fresh vegetables scattered across the top edge: capsicums, tomatoes, mushrooms, lettuce and onion"></div>
  <div class="produce-bottom" role="img" aria-label="Fresh vegetables across the bottom edge: capsicums, tomatoes, onion, lettuce, mushrooms and garlic"></div>

  <main class="site">
    <div class="promo-bar">You can place your order over the phone. easy!</div>
    <header class="header">
      <div class="brand">Crispfield</div>
      <nav class="main-nav">
        <a class="active" href="#">HOME</a>
        <a href="#">OUR CUSTOMERS</a>
        <a href="#">ABOUT CRISPFIELD</a>
        <a href="#">CONTACT US</a>
      </nav>
      <div class="call">
        <div class="call-icon">
          <svg width="14" height="14" viewBox="0 0 24 24"><path fill="#fff" d="M6.6 10.8a15.1 15.1 0 0 0 6.6 6.6l2.2-2.2a1 1 0 0 1 1-.25 11.4 11.4 0 0 0 3.6.57 1 1 0 0 1 1 1V20a1 1 0 0 1-1 1A17 17 0 0 1 3 4a1 1 0 0 1 1-1h3.5a1 1 0 0 1 1 1c0 1.25.2 2.45.57 3.57a1 1 0 0 1-.25 1z"/></svg>
        </div>
        <div>
          <div class="call-label">Call us now</div>
          <div class="call-number">02 5550 1384</div>
        </div>
      </div>
    </header>

    <div class="body">
      <aside class="categories">
        <h2>ALL CATEGORIES</h2>
        <ul>
          <li>POTATOES</li><li>PUMPKIN</li><li>CARROT</li><li>ONION</li><li>CABBAGE</li>
          <li>CELERY</li><li>CAPSICUM</li><li>ZUCCHINI</li><li>MUSHROOM</li><li>SPINACH</li>
          <li>BROCOLLI</li><li>CAULIFLOWER</li><li>MIXES</li>
        </ul>
      </aside>
      <section class="hero" role="img" aria-label="Wooden crate overflowing with fresh vegetables: cauliflower, capsicums, radishes, zucchini, tomatoes and turnips">
        <h1 class="hero-title">Fresh is Best !</h1>
      </section>
    </div>

    <section class="why">
      <h2>Why Choose us?</h2>
      <div class="reason one">
        <svg width="30" height="30" viewBox="0 0 30 30" fill="none" stroke="#fff" stroke-width="1.4"><circle cx="16" cy="17" r="10"/><path d="M16 17V11M16 17l4 2M13 4h6M16 4v3M2 14h5M1 18h5M3 22h5"/></svg>
        <span>Consistantly cut vegies<br>everytime</span>
      </div>
      <div class="reason two">
        <svg width="32" height="30" viewBox="0 0 32 30" fill="none" stroke="#fff" stroke-width="1.4"><path d="M18 2l7 3v5c0 4-3 7-7 8-4-1-7-4-7-8V5z"/><path d="M15 9l2 2 4-4"/><path d="M2 20h4v8H2zM6 21h6l5 2h4a2 2 0 0 1 0 4h-7M6 27h10l12-6"/></svg>
        <span>We use fresh,<br>quality products</span>
      </div>
      <div class="reason three">
        <svg width="36" height="28" viewBox="0 0 36 28" fill="none" stroke="#fff" stroke-width="1.4"><path d="M4 3h20v17H4zM24 9h6l4 5v6H24"/><circle cx="9" cy="22" r="3"/><circle cx="28" cy="22" r="3"/><path d="M10 11l3 3 6-6M0 8h3M0 13h3"/></svg>
        <span>We can deliver to your<br>premises</span>
      </div>
    </section>
  </main>

  <footer class="footer">
    <div class="footer-cats">
      <span>POTATOES</span><span>PUMPKIN</span><span>CARROT</span><span>ONION</span><span>CABBAGE</span><span>CELERY</span><span>CAPSICUM</span><span>ZUCCHINI</span><span>MUSHROOM</span><span>SPINACH</span><span>BROCOLLI</span><span>CAULIFLOWER</span><span>MIXES</span>
    </div>
    <nav class="footer-nav">
      <span>HOME</span><span>OUR CUSTOMERS</span><span>ABOUT CRISPFIELD</span><span>CONTACT US</span>
    </nav>
    <p class="copyright">© copyrights 2023 <span class="name">Crispfield</span> &nbsp;|&nbsp;&nbsp;&nbsp; All rights reserved.</p>
  </footer>
</body>
</html>
```